Letter Head Design - Finance industry

Design a letterhead to match the logo. Needs to be clean, simple and crisp. I'm open to suggestions. Will be using the logo that was submitted last with the W crossed over

Target Market(s)

Small medium businesses and government department's

Industry/Entity Type

Industry

Font styles to use
Sans Serif

Colors
cadf82
bcd85c
acd036
9bcb3c
e9e9e9
aaaaaa
000000
7f7f7f
b7b7b7

Requirements
Must have
• Need to display: Logo, Business address, ABN number, ASIC register number, contact phone, website, company email. Details are as per below:

Suite 4B Level 17
Marlowe Crest Tower
9 Kestin Lane
Sydney NSW 2000
Landline Ph: 02 9417 3065
Ph: 1300 5914 37
Email: enquiries@corvalmoney.com.au
W: www.corvalmoney.com.au

On the footer, the details below need to be specified:
ABN: 48 703 591 236
ASIC Registration Number: 73 418806521

Should not have
• No imagery or design that is not in line with the logo

```html
<!DOCTYPE html>
<html lang="en">
<head>
<meta charset="utf-8">
<title>Corval Money Letterhead</title>
<link rel="stylesheet" href="https://fonts.googleapis.com/css2?family=Arimo:wght@400&display=swap">
<style>
  :root {
    --leaf-green: #acd036;
    --paper: #ffffff;
    --ink: #000000;
    --brand-grey: #7f7f7f;
    --on-green: #ffffff;
  }
  html, body {
    margin: 0;
    padding: 0;
    overflow: hidden;
    background: var(--paper);
  }
  .letterhead {
    position: relative;
    width: 927px;
    height: 1200px;
    overflow: hidden;
    background: var(--paper);
    font-family: "Arimo", Arial, sans-serif;
  }
  .band { position: absolute; background: var(--leaf-green); }
  .band--header-edge { left: 0; top: 0; width: 55px; height: 133px; }
  .band--header-main { left: 349px; top: 0; width: 578px; height: 133px; }
  .band--footer-left { left: 0; top: 1099px; width: 334px; height: 27px; }
  .band--footer-right { left: 593px; top: 1099px; width: 334px; height: 27px; }

  .brand {
    position: absolute;
    left: 118px;
    top: 38px;
    display: flex;
    align-items: center;
    gap: 12px;
  }
  .brand__dot {
    width: 44px;
    height: 44px;
    border-radius: 50%;
    background: var(--leaf-green);
  }
  .brand__name {
    font-size: 27px;
    line-height: 1.1;
    color: var(--brand-grey);
  }

  .contact {
    position: absolute;
    top: 33px;
    margin: 0;
    font-size: 16px;
    line-height: 20px;
    color: var(--on-green);
    font-style: normal;
  }
  .contact--address { left: 378px; }
  .contact--lines { left: 625px; }
  .contact__divider {
    position: absolute;
    left: 599px;
    top: 36px;
    width: 1px;
    height: 73px;
    background: var(--on-green);
  }

  .footer-mark {
    position: absolute;
    left: 436px;
    top: 1077px;
    width: 56px;
    height: 56px;
    border-radius: 50%;
    background: var(--leaf-green);
  }
  .registration {
    position: absolute;
    left: 596px;
    top: 1140px;
    margin: 0;
    font-size: 16px;
    line-height: 22px;
    color: var(--ink);
  }
</style>
</head>
<body>
<main class="letterhead">
  <header>
    <div class="band band--header-edge"></div>
    <div class="brand">
      <span class="brand__dot"></span>
      <span class="brand__name">Corval<br>Money</span>
    </div>
    <div class="band band--header-main"></div>
    <address class="contact contact--address">
      Address: Suite 4B Level 17<br>
      Marlowe Crest Tower<br>
      9 Kestin Lane<br>
      Sydney NSW 2000
    </address>
    <div class="contact__divider"></div>
    <p class="contact contact--lines">
      Landline Ph: 02 9417 3065<br>
      Ph: 1300 5914 37<br>
      Email: enquiries@corvalmoney.com.au<br>
      web: www.corvalmoney.com.au
    </p>
  </header>

  <footer>
    <div class="band band--footer-left"></div>
    <div class="footer-mark"></div>
    <div class="band band--footer-right"></div>
    <p class="registration">
      ABN: 48 703 591 236<br>
      ASIC Registration Number: 73 418806521
    </p>
  </footer>
</main>
</body>
</html>
```